A layout of a webpage for oil trade platform

I would like to have a desgin of one page webpage (with section scrollling dowin) that woulf present the new product i.e. oil trade platform for wholesale buyers and sellers.
Layout should consist of the sections similar to the given at: https://strona.trawomirek.pl/modul-planowania-spotkan
However oil industy require more colors and more photo stories than here for doctor.
I. I woul imagine at first below menu a slider with brueg information about the product and its advantages with "more" button next to the prict screen of our platform on different displays (PC and mobile).
II. Bellow the slider I would imagine icons correspoing to the advantages of that plaftorm:
1. Purchase/sale process automation 24/7
2. Access to the best deals
3. Electronic offerings and orderings
4. Transaction status monitoring
5. Data and transaction security
II A) (optional):
In near future we would like to prepare a short video presenation. Hence please prepare a place to display that element here.
At the moment alternatvily please prepare a How it works section that would explan the platform operating process
III. Next secion is about benefits for Oil Purchaser
It can be done either by icons of by text and corresponding grahip for while section.
Benefits:
- Access to cheaper oil
- Convenience of online orders
- Possibility to compare prices on the market
- Transaction history
- Order status monitoring
- Seccurity and transparency of purchase
IV. Next seciont is about benefits for Oil Seller
Benefits:
- New sale channel
- Attracting new clients
- More oil sold
- Transaction security
- Possibility to integrate with distribution infrastructure and logistits for more efficient automation.
V. Contact form
VI. Footer
I would need a layout that that will correspond to the very dynamic logo but I would expect also a clean form, smoth and modern. It has to be proffessional layout with more corporate character.
It can use a paralax features if needed.
Attachments:
- logo design
- platfrom print screen
Industry/Entity Type
Oil And Gas
Number of Pages Required
1 page

```html
<!DOCTYPE html>
<html lang="en">
<head>
<meta charset="utf-8">
<title>Crudora – Oil Trade Platform</title>
<link href="https://fonts.googleapis.com/css2?family=Nunito+Sans:wght@400;600;700&display=swap" rel="stylesheet">
<style>
:root{
  --orange:#f05a28;
  --orange-light:#f47c3c;
  --navy:#1c2b55;
  --navy-deep:#0f2246;
  --hero-blue:#1d4784;
  --text:#5a5f6b;
  --muted:#8b8f98;
  --line:#dcdfe4;
  --panel:#f5f5f6;
  --footer:#f3f3f4;
  --white:#ffffff;
  --screen:#dfe5ee;
  --device:#14181f;
}
*{box-sizing:border-box;margin:0;padding:0}
html,body{width:1200px;height:3285px;overflow:hidden}
body{font-family:"Nunito Sans",Arial,sans-serif;color:var(--text);background:var(--white);position:relative}
a{text-decoration:none}
.btn{position:absolute;display:flex;align-items:center;justify-content:center;gap:10px;color:var(--white);font-weight:700;font-size:15px;letter-spacing:.5px;text-transform:uppercase;background:linear-gradient(180deg,var(--orange-light),var(--orange));border-radius:2px}

/* hero */
.hero{position:absolute;left:0;top:0;width:1200px;height:668px;background:linear-gradient(160deg,var(--hero-blue) 0%,#173a70 45%,var(--navy-deep) 100%);overflow:hidden}
.brand{position:absolute;display:flex;align-items:center;gap:12px;font-weight:700;font-size:30px;letter-spacing:.5px}
.brand-mark{width:44px;height:44px;border-radius:50%;background:var(--orange)}
.hero .brand{left:77px;top:34px;color:var(--white)}
.nav{position:absolute;right:58px;top:44px;display:flex;gap:6px}
.nav a{color:var(--white);font-size:13px;font-weight:700;padding:10px 14px;letter-spacing:.3px}
.nav a.active{background:var(--orange)}
.hero h1{position:absolute;left:75px;top:252px;width:480px;color:var(--white);font-size:33px;line-height:40px;font-weight:700}
.hero .lead{position:absolute;left:75px;top:346px;width:440px;color:#e6ecf6;font-size:18px;line-height:27px}
.hero .btn{left:75px;top:458px;width:151px;height:48px;font-size:17px}
.monitor{position:absolute;left:596px;top:186px;width:604px;height:350px;background:var(--device);border:12px solid var(--device)}
.monitor-screen{width:100%;height:100%;background:var(--screen)}
.monitor-stand{position:absolute;left:840px;top:536px;width:150px;height:120px;background:var(--device)}
.laptop{position:absolute;left:430px;top:429px;width:344px;height:220px;background:var(--device);border:10px solid var(--device);border-radius:8px 8px 0 0}
.laptop-screen{width:100%;height:100%;background:var(--screen)}
.laptop-base{position:absolute;left:394px;top:649px;width:416px;height:12px;background:#c9ced6;border-radius:0 0 10px 10px}
.phone{position:absolute;left:1069px;top:429px;width:110px;height:228px;background:var(--device);border-radius:14px;padding:28px 6px}
.phone-screen{width:100%;height:100%;background:var(--screen)}

/* features */
.features{position:absolute;left:58px;top:668px;width:1084px;height:193px;display:grid;grid-template-columns:repeat(5,1fr)}
.feature{display:flex;flex-direction:column;align-items:center;padding-top:36px;text-align:center}
.feature svg{width:60px;height:60px}
.feature p{margin-top:14px;font-size:15px;line-height:22px;font-weight:600;color:#4d5260}

/* how it works */
.how{position:absolute;left:0;top:861px;width:1200px;height:427px;background:var(--panel)}
.tablet{position:absolute;left:75px;top:43px;width:483px;height:340px;background:#2e3646;border-radius:14px}
.tablet-screen{position:absolute;left:28px;top:22px;width:404px;height:296px;background:linear-gradient(180deg,#e9ecef,#cfe0c6 55%,#e4e7ea)}
.tablet-btn{position:absolute;right:10px;top:160px;width:20px;height:20px;border-radius:50%;background:var(--white)}
.play{position:absolute;left:201px;top:140px;width:74px;height:74px}
.section-title{position:absolute;color:var(--navy);font-weight:700;font-size:27px}
.how .section-title{left:613px;top:82px}
.how .body{position:absolute;left:613px;top:135px;width:520px;font-size:14.5px;line-height:24px;color:var(--muted)}
.how .btn{left:613px;top:282px;width:243px;height:55px;font-size:14px}

/* benefits */
.benefits{position:absolute;left:0;width:1200px;height:528px}
.buyer{top:1288px;height:527px;background:var(--white)}
.seller{top:1815px;background:var(--panel)}
.photo{position:absolute;top:0;height:100%}
.buyer .photo{left:613px;width:587px;background:linear-gradient(160deg,#f2a86a 0%,#d4713a 35%,#3b4a63 70%,#2a3242 100%)}
.seller .photo{left:0;width:587px;background:linear-gradient(180deg,#1a4f9a 0%,#c9a23a 45%,#e0b640 55%,#133c7c 100%)}
.buyer .section-title{left:73px;top:60px;font-size:25px}
.seller .section-title{left:635px;top:70px;font-size:25px}
.benefit-list{position:absolute;list-style:none}
.benefit-list li{display:flex;align-items:center;font-size:14.5px;font-weight:600;color:#4d5260;line-height:22px}
.benefit-list svg{width:30px;height:30px;flex:none;margin-right:22px}
.buyer .benefit-list{left:80px;top:123px}
.buyer .benefit-list li{height:60px}
.seller .benefit-list{left:642px;top:145px}
.seller .benefit-list li{height:61px;width:450px}

/* contact */
.contact{position:absolute;left:0;top:2343px;width:1200px;height:504px}
.contact h2{position:absolute;left:0;width:1200px;top:66px;text-align:center;color:var(--navy);font-size:28px;font-weight:700}
.contact .sub{position:absolute;left:0;width:1200px;top:127px;text-align:center;font-size:14px;color:var(--text)}
.field{position:absolute;border:1px solid var(--line);background:var(--white);font-size:13px;color:#555;padding:12px 12px}
.contact .btn{left:480px;top:386px;width:240px;height:54px;font-size:14px}

/* footer */
.footer{position:absolute;left:0;top:2847px;width:1200px;height:438px;background:var(--footer)}
.footer .brand{left:77px;top:72px;color:var(--navy);font-size:26px}
.footer .brand-mark{width:38px;height:38px}
.address{position:absolute;left:77px;top:140px;font-size:14px;line-height:23px;color:var(--text)}
.contact-line{position:absolute;left:77px;display:flex;align-items:center;gap:18px;font-size:14px;color:var(--orange)}
.contact-line svg{width:14px;height:14px}
.socials{position:absolute;left:77px;top:285px;display:flex;gap:18px}
.socials span{width:14px;height:14px;border-radius:50%;background:#9aa0aa}
.foot-col{position:absolute;top:52px}
.foot-col h4{font-size:13px;font-weight:700;color:var(--navy);letter-spacing:.4px;margin-bottom:14px}
.foot-col ul{list-style:none}
.foot-col li{font-size:13.5px;line-height:30.7px;color:var(--text)}
.newsletter-input{position:absolute;left:883px;top:90px;width:243px;height:41px;border:1px solid var(--line);background:var(--white);font-size:13px;padding:11px 10px;color:#555}
.footer .btn{left:1036px;top:142px;width:90px;height:42px;font-size:13px}
.footer-rule{position:absolute;left:77px;top:339px;width:1049px;height:1px;background:var(--line)}
.copyright{position:absolute;left:0;width:1200px;top:382px;text-align:center;font-size:12px;color:var(--muted)}
</style>
</head>
<body>

<header class="hero">
  <div class="brand"><span class="brand-mark"></span>Crudora</div>
  <nav class="nav">
    <a class="active" href="#">HOME</a><a href="#">ABOUT US</a><a href="#">SERVICES</a><a href="#">HOW IT WORKS</a><a href="#">BENEFITS</a><a href="#">BLOG</a><a href="#">CONTACT US</a>
  </nav>
  <div class="monitor"><div class="monitor-screen" role="img" aria-label="Platform orders dashboard on a desktop monitor"></div></div>
  <div class="monitor-stand"></div>
  <div class="laptop"><div class="laptop-screen" role="img" aria-label="Platform orders dashboard on a laptop"></div></div>
  <div class="laptop-base"></div>
  <div class="phone"><div class="phone-screen" role="img" aria-label="Platform orders dashboard on a mobile phone"></div></div>
  <h1>Nam fermentum vestibulum amet turpis tincidunt.</h1>
  <p class="lead">Aliquam molestie, mi et imperdiet euismod, dui purus auctor tellus, et interdum lacus lectus et ante dignissim lectus vitae.</p>
  <a class="btn" href="#">More
    <svg width="12" height="14" viewBox="0 0 12 14"><path d="M3 1l6 6-6 6" fill="none" stroke="#fff" stroke-width="3"/></svg>
  </a>
</header>

<section class="features">
  <div class="feature">
    <svg viewBox="0 0 60 60"><circle cx="30" cy="30" r="27" fill="none" stroke="#1c2b55" stroke-width="2"/><circle cx="30" cy="30" r="16" fill="none" stroke="#1c2b55" stroke-width="2"/><path d="M30 20v10h8" fill="none" stroke="#1c2b55" stroke-width="2"/></svg>
    <p>Purchase/sale process<br>automation 24/7</p>
  </div>
  <div class="feature">
    <svg viewBox="0 0 60 60"><path d="M12 28h9v24h-9z M21 30l9-14c2-4 7-3 6 2l-2 9h14c3 0 5 3 4 5l-4 16c-1 3-3 4-6 4H21" fill="none" stroke="#1c2b55" stroke-width="2" stroke-linejoin="round"/></svg>
    <p>Access to the best<br>deals</p>
  </div>
  <div class="feature">
    <svg viewBox="0 0 60 60"><rect x="6" y="6" width="48" height="48" rx="8" fill="none" stroke="#1c2b55" stroke-width="2"/><path d="M20 42l3-9 17-17 6 6-17 17z M37 19l6 6" fill="none" stroke="#1c2b55" stroke-width="2" stroke-linejoin="round"/></svg>
    <p>Electronic offerings<br>and orderings</p>
  </div>
  <div class="feature">
    <svg viewBox="0 0 60 60"><rect x="12" y="14" width="36" height="24" rx="2" fill="none" stroke="#1c2b55" stroke-width="2"/><path d="M4 44h52l-4 5H8z" fill="none" stroke="#1c2b55" stroke-width="2" stroke-linejoin="round"/></svg>
    <p>Transaction status<br>monitoring</p>
  </div>
  <div class="feature">
    <svg viewBox="0 0 60 60"><path d="M12 8h36v22c0 12-9 19-18 24-9-5-18-12-18-24z" fill="none" stroke="#1c2b55" stroke-width="2"/><path d="M30 12v38" stroke="#1c2b55" stroke-width="2"/></svg>
    <p>Data and transaction<br>security</p>
  </div>
</section>

<section class="how">
  <div class="tablet">
    <div class="tablet-screen" role="img" aria-label="Platform analytics dashboard with sales chart, placeholder for video presentation"></div>
    <svg class="play" viewBox="0 0 74 74"><circle cx="37" cy="37" r="33" fill="rgba(0,0,0,.25)" stroke="#fff" stroke-width="5"/><path d="M30 23l20 14-20 14z" fill="#fff"/></svg>
    <span class="tablet-btn"></span>
  </div>
  <h2 class="section-title">How it Works</h2>
  <p class="body">Aliquam molestie, mi et imperdiet euismod, dui purus auctor tellus, et interdum lacus lectus et ante. Sed accumsan sollicitudin sapien, sit amet adipiscing turpis gravida ac. In congue, neque ac lobortis volutpat, libero mauris varius mi, vitae suscipit ipsum ligula vitae risus.</p>
  <a class="btn" href="#">See how it works</a>
</section>

<section class="benefits buyer">
  <h2 class="section-title">Benefits for Oil Purchaser</h2>
  <ul class="benefit-list">
    <li><svg viewBox="0 0 30 30"><circle cx="9" cy="9" r="6" fill="none" stroke="#f05a28" stroke-width="2.5"/><path d="M13 13l13 13M20 20l-3 3M24 24l-3 3" stroke="#f05a28" stroke-width="2.5"/></svg>Access to cheaper oil</li>
    <li><svg viewBox="0 0 30 30"><path d="M22 5h-17v21h21v-13" fill="none" stroke="#f05a28" stroke-width="2.5"/><path d="M11 19l2-6 12-12 4 4-12 12z" fill="#f05a28"/></svg>Convenience of online orders</li>
    <li><svg viewBox="0 0 30 30"><path d="M3 10h22M19 4l6 6-6 6M27 21H5M11 15l-6 6 6 6" fill="none" stroke="#f05a28" stroke-width="2.5"/></svg>Possibility to compare prices on the market</li>
    <li><svg viewBox="0 0 30 30"><circle cx="15" cy="15" r="12" fill="none" stroke="#f05a28" stroke-width="2.5"/><path d="M15 8v7h6" fill="none" stroke="#f05a28" stroke-width="2.5"/></svg>Transaction history</li>
    <li><svg viewBox="0 0 30 30"><rect x="5" y="6" width="20" height="14" fill="none" stroke="#f05a28" stroke-width="2.5"/><path d="M1 24h28" stroke="#f05a28" stroke-width="2.5"/></svg>Order status monitoring</li>
    <li><svg viewBox="0 0 30 30"><path d="M5 3h20v13c0 6-5 10-10 12-5-2-10-6-10-12z" fill="#f05a28"/><path d="M15 5v21" stroke="#fff" stroke-width="2"/></svg>Security and transparency of purchase</li>
  </ul>
  <div class="photo" role="img" aria-label="Oil tank train cars moving on rails at sunset"></div>
</section>

<section class="benefits seller">
  <div class="photo" role="img" aria-label="Offshore oil platform lit up at night over the sea"></div>
  <h2 class="section-title">Benefits for Oil Seller</h2>
  <ul class="benefit-list">
    <li><svg viewBox="0 0 30 30"><rect x="11" y="3" width="8" height="7" fill="#f05a28"/><rect x="2" y="20" width="8" height="7" fill="#f05a28"/><rect x="11" y="20" width="8" height="7" fill="#f05a28"/><rect x="20" y="20" width="8" height="7" fill="#f05a28"/><path d="M15 10v10M6 20v-5h18v5" fill="none" stroke="#f05a28" stroke-width="2"/></svg>New sale channel</li>
    <li><svg viewBox="0 0 30 30"><circle cx="15" cy="8" r="5" fill="#f05a28"/><circle cx="6" cy="11" r="3.5" fill="#f05a28"/><circle cx="24" cy="11" r="3.5" fill="#f05a28"/><path d="M7 27c0-7 3-12 8-12s8 5 8 12z M0 25c0-5 2-9 6-9 2 0 3 1 3 1-2 2-3 5-3 8z M30 25c0-5-2-9-6-9-2 0-3 1-3 1 2 2 3 5 3 8z" fill="#f05a28"/></svg>Attracting new clients</li>
    <li><svg viewBox="0 0 30 30"><path d="M15 2c4 7 9 12 9 18a9 9 0 0 1-18 0c0-6 5-11 9-18z" fill="#f05a28"/></svg>More oil sold</li>
    <li><svg viewBox="0 0 30 30"><path d="M9 13V9a6 6 0 0 1 12 0v4" fill="none" stroke="#f05a28" stroke-width="3"/><rect x="5" y="13" width="20" height="15" rx="2" fill="#f05a28"/></svg>Transaction security</li>
    <li><svg viewBox="0 0 30 30"><circle cx="11" cy="17" r="7" fill="none" stroke="#f05a28" stroke-width="5" stroke-dasharray="3 2.5"/><circle cx="11" cy="17" r="3" fill="#f05a28"/><circle cx="23" cy="7" r="4" fill="none" stroke="#f05a28" stroke-width="3.5" stroke-dasharray="2 1.6"/></svg>Possibility to integrate with distribution infrastructure and logistits for more efficient automation.</li>
  </ul>
</section>

<section class="contact">
  <h2>Contact Us</h2>
  <p class="sub">Vestibulum vel metus sit amet turpis bibendum tincidunt vel sit amet quam</p>
  <div class="field" style="left:164px;top:191px;width:423px;height:46px">Name</div>
  <div class="field" style="left:164px;top:246px;width:423px;height:46px">Email Address</div>
  <div class="field" style="left:164px;top:300px;width:423px;height:47px">Phone No</div>
  <div class="field" style="left:613px;top:191px;width:423px;height:156px">Message</div>
  <a class="btn" href="#">See how it works</a>
</section>

<footer class="footer">
  <div class="brand"><span class="brand-mark"></span>Crudora</div>
  <p class="address">412 Harbour Lane,<br>Dunmore, K07 3LP</p>
  <div class="contact-line" style="top:198px"><svg viewBox="0 0 14 14"><rect x="1" y="3" width="12" height="9" fill="#f05a28"/><path d="M1 3l6 5 6-5" fill="none" stroke="#fff" stroke-width="1.2"/></svg>info@crudora-trade.com</div>
  <div class="contact-line" style="top:231px"><svg viewBox="0 0 14 14"><path d="M7 1a4.5 4.5 0 0 1 4.5 4.5C11.5 9 7 13 7 13S2.5 9 2.5 5.5A4.5 4.5 0 0 1 7 1z" fill="#f05a28"/><circle cx="7" cy="5.5" r="1.6" fill="#fff"/></svg>Map Location</div>
  <div class="socials"><span></span><span></span><span></span><span></span><span></span><span></span></div>

  <div class="foot-col" style="left:379px">
    <h4>SITE MAP</h4>
    <ul><li>Home</li><li>About Us</li><li>Services</li><li>How it Works</li><li>Benefits</li><li>Blog</li><li>Contact Us</li></ul>
  </div>
  <div class="foot-col" style="left:618px">
    <h4>RESOURCES</h4>
    <ul><li>Aliquam molestie</li><li>Perdiet euismod</li><li>Dui purus auctor tellus</li><li>Dum lacus lectus</li></ul>
  </div>
  <div class="foot-col" style="left:883px">
    <h4>NEWSLETTER SIGN UP</h4>
  </div>
  <div class="newsletter-input">Enter Email Address</div>
  <a class="btn" href="#">Sign up</a>

  <div class="footer-rule"></div>
  <p class="copyright">Copyright © 2017. Company Name. All Right Reserved</p>
</footer>

</body>
</html>
```